Fern Tone & Glow - Business Banner with Brand Elements

Design:
• We would like to get a creative design for a wide banner that will go outside our medical spa clinic location. We need a designer to make a simple yet colorful and high-quality design layout. We want this banner to be eye-catching and to communicate the services we offer at our business: Laser Hair Removal | Kelvra | Lip Filler.

Requirements:
• We would like the banner to include our companies information which is the following:

Logo
“Refresh Your Skin”
Laser Hair Removal | Kelvra | Lip Filler
(555) 286-1937
www.FernToneGlow.com

Colors:
• Our business colors are orange, a hint of black and white, but mostly peach/orange tones. (Orange: #f78f20 , White: #ffffff)

Fonts:
• Josefins Sans Bold & Lato

Content and images can be located here:
https://files.cloudvaultex.net/shared/folders/7xQpLm2Vb9RtK4nYsWd3Hc8ZuJe5Ga1Tf?view=open

The following will give you an idea of our brand presentation:
• Our website is: www.FernToneGlow.com
• Our Instagram; @ferntoneglow
• Our Facebook: www.friendloop.net/ferntoneglow

Target Market(s)
• Women 25 - 45

Industry/Entity Type
• Beauty

```html
<!DOCTYPE html>
<html lang="en">
<head>
<meta charset="utf-8">
<title>Fern Tone &amp; Glow – Outdoor Banner</title>
<link rel="stylesheet" href="https://fonts.googleapis.com/css2?family=Josefin+Sans:wght@400;700&family=Lato:wght@400;700&display=swap">
<style>
  :root {
    --orange: #f78f20;
    --orange-deep: #e57a10;
    --white: #ffffff;
    --ink: #2b2b2b;
    --stage: #e4e4e4;
    --sky-top: #5dbddf;
    --sky-mid: #b9e3f1;
    --sand: #eef1f1;
  }
  * { box-sizing: border-box; margin: 0; padding: 0; }
  html, body {
    width: 1200px;
    height: 818px;
    overflow: hidden;
    background: var(--stage);
  }
  .banner {
    position: absolute;
    left: 0;
    top: 184px;
    width: 1200px;
    height: 450px;
    overflow: hidden;
    font-family: "Josefin Sans", "Lato", sans-serif;
  }
  .hero-photo {
    position: absolute;
    inset: 0;
    background: linear-gradient(180deg, var(--sky-top) 0%, var(--sky-mid) 55%, var(--sand) 72%, var(--sand) 100%);
  }
  .banner-shapes {
    position: absolute;
    inset: 0;
    width: 100%;
    height: 100%;
  }
  .headline {
    position: absolute;
    left: 50px;
    top: 38px;
    color: var(--white);
    line-height: 1;
  }
  .headline-script {
    display: block;
    font-weight: 400;
    font-size: 112px;
    letter-spacing: 1px;
  }
  .headline-bold {
    display: block;
    margin-top: 6px;
    font-weight: 700;
    font-size: 66px;
    letter-spacing: 1px;
  }
  .service-row {
    position: absolute;
    left: 48px;
    display: flex;
    gap: 9px;
  }
  .service-row--top { top: 232px; }
  .service-row--bottom { top: 298px; }
  .service {
    height: 50px;
    border-radius: 25px;
    background: var(--white);
    display: flex;
    align-items: center;
    padding: 0 22px 0 6px;
    color: var(--ink);
    font-weight: 700;
    font-size: 25px;
    letter-spacing: 0.3px;
    white-space: nowrap;
  }
  .service-dot {
    width: 38px;
    height: 38px;
    border-radius: 50%;
    background: var(--orange);
    margin-right: 10px;
    flex: none;
  }
  .service-label { padding-top: 4px; }
  .service--laser { width: 409px; }
  .service--laser .service-dot { margin-right: 16px; }
  .contact {
    position: absolute;
    left: 50px;
    top: 385px;
    display: flex;
    align-items: center;
    gap: 10px;
    color: var(--white);
    font-weight: 700;
    font-size: 22px;
  }
  .contact svg { width: 24px; height: 24px; flex: none; }
  .contact-text { padding-top: 4px; }
  .contact-divider {
    width: 2px;
    height: 24px;
    background: var(--white);
    margin: 0 6px;
  }
  .brand {
    position: absolute;
    left: 975px;
    top: 250px;
    width: 195px;
    display: flex;
    flex-direction: column;
    align-items: center;
  }
  .brand-mark {
    width: 62px;
    height: 62px;
    border-radius: 50%;
    background: var(--orange);
    margin-bottom: 12px;
  }
  .brand-name {
    color: var(--ink);
    font-weight: 700;
    font-size: 31px;
    line-height: 1.05;
    text-align: center;
  }
</style>
</head>
<body>
  <section class="banner">
    <div class="hero-photo" role="img" aria-label="Photograph of a smiling woman in a straw sun hat on a bright sunny beach with blue sea and sky"></div>

    <svg class="banner-shapes" viewBox="0 0 1838 690" preserveAspectRatio="none" aria-hidden="true">
      <path fill="var(--orange-deep)" d="M0,0 H625 C730,20 795,90 790,210 C786,290 742,335 748,405 C760,525 880,590 1030,588 C1230,585 1420,440 1610,378 C1710,348 1785,350 1838,370 V690 H0 Z"/>
      <path fill="var(--orange)" d="M0,0 H605 C705,20 770,85 768,205 C766,285 720,330 725,400 C735,520 850,575 1000,572 C1200,568 1400,430 1600,368 C1700,340 1780,342 1838,362 V690 H0 Z"/>
      <path fill="var(--orange-deep)" d="M840,690 C1100,650 1300,520 1500,430 C1650,365 1760,350 1838,378 V395 C1760,372 1650,385 1505,450 C1300,540 1110,660 880,690 Z"/>
      <path fill="var(--white)" d="M880,690 C1110,660 1300,540 1505,450 C1650,385 1760,372 1838,395 V690 Z"/>
    </svg>

    <h1 class="headline">
      <span class="headline-script">Refresh</span>
      <span class="headline-bold">YOUR SKIN</span>
    </h1>

    <div class="service-row service-row--top">
      <div class="service service--laser"><span class="service-dot"></span><span class="service-label">LASER HAIR REMOVAL</span></div>
    </div>
    <div class="service-row service-row--bottom">
      <div class="service service--kelvra"><span class="service-dot"></span><span class="service-label">KELVRA</span></div>
      <div class="service service--lip"><span class="service-dot"></span><span class="service-label">LIP FILLER</span></div>
    </div>

    <div class="contact">
      <svg viewBox="0 0 24 24" fill="none" stroke="var(--white)" stroke-width="1.6" stroke-linejoin="round" aria-hidden="true">
        <path d="M5 3h4l2 5-2.5 1.5a11 11 0 0 0 6 6L16 13l5 2v4a2 2 0 0 1-2 2A17 17 0 0 1 3 5a2 2 0 0 1 2-2z"/>
      </svg>
      <span class="contact-text">(555) 286-1937</span>
      <span class="contact-divider"></span>
      <svg viewBox="0 0 24 24" fill="none" stroke="var(--white)" stroke-width="1.6" aria-hidden="true">
        <circle cx="12" cy="12" r="9"/>
        <ellipse cx="12" cy="12" rx="4" ry="9"/>
        <path d="M3 12h18"/>
      </svg>
      <span class="contact-text">www.FernToneGlow.com</span>
    </div>

    <div class="brand">
      <span class="brand-mark"></span>
      <span class="brand-name">Fern Tone<br>&amp; Glow</span>
    </div>
  </section>
</body>
</html>
```